Quiet Verses Across Winter Evenings

Need a BOOK COVER, SPINE, and BACK for above named book. This is the story of my late wife (a university professor) told through her own songs and poems. It is about the people she loved, especially her grand children, her extensive professional and life interests, her family, friends, and festivities, her illness, etc.
Updates

Need extra days to review

Target Market(s)

Family and friends

Font styles to use
Other font styles liked:
• Times New Roman

Requirements
Must have
• Regret I haven't given much thought to it...
Nice to have
• Regret I haven't given much thought to it..
Should not have

```html
<!DOCTYPE html>
<html lang="en">
<head>
<meta charset="utf-8">
<title>Quiet Verses Across Winter Evenings — Book Cover</title>
<link href="https://fonts.googleapis.com/css2?family=Great+Vibes&family=Noto+Serif:wght@400&display=swap" rel="stylesheet">
<style>
  :root {
    --brick: #b33523;
    --flame: #e04321;
    --blush: #f29c94;
    --ink: #1c1410;
    --paper: #ffffff;
    --rule: #e04321;
    --photo-light: #8d8a74;
    --photo-mid: #4a5430;
    --photo-dark: #1f2a14;
  }
  html, body {
    margin: 0;
    padding: 0;
    overflow: hidden;
    background: #ffffff;
  }
  .cover {
    position: relative;
    width: 1200px;
    height: 873px;
    overflow: hidden;
    font-family: "Noto Serif", Georgia, serif;
  }
  .block { position: absolute; }
  .script { font-family: "Great Vibes", cursive; font-weight: 400; word-spacing: 0.18em; }

  /* Back cover */
  .back-top    { left: 0; top: 0; width: 575px; height: 55px; background: var(--brick); }
  .back-field  { left: 0; top: 55px; width: 575px; height: 660px; background: var(--blush); }
  .back-bottom { left: 0; top: 715px; width: 575px; height: 158px; background: var(--brick); }
  .back-title {
    left: 100px; top: 136px;
    font-size: 38px; color: var(--paper); line-height: 1; white-space: nowrap;
  }
  .back-subtitle {
    left: 200px; top: 176px;
    font-size: 19px; color: var(--ink); white-space: nowrap;
  }
  .back-blurb {
    left: 102px; top: 234px; width: 372px;
    font-size: 12.3px; line-height: 16.6px; color: var(--ink);
    margin: 0; letter-spacing: 0.55px;
  }

  /* Spine */
  .spine-top    { left: 575px; top: 0; width: 55px; height: 560px; background: var(--brick); }
  .spine-bottom { left: 575px; top: 560px; width: 55px; height: 313px; background: var(--flame); }
  .spine-title {
    left: 575px; top: 57px; width: 55px; height: 480px;
    writing-mode: vertical-rl;
    display: flex; align-items: center; justify-content: flex-start;
    color: var(--paper); white-space: nowrap;
  }
  .spine-title .script { font-size: 30px; margin-bottom: 18px; }
  .spine-title .serif { font-size: 21px; letter-spacing: 0.5px; }
  .spine-author {
    left: 575px; top: 598px; width: 55px; height: 235px;
    writing-mode: vertical-rl;
    display: flex; align-items: center;
    font-size: 15.5px; color: var(--paper); letter-spacing: 1px; white-space: nowrap;
  }

  /* Front cover */
  .front-top    { left: 630px; top: 0; width: 570px; height: 55px; background: var(--flame); }
  .front-field  { left: 630px; top: 55px; width: 570px; height: 282px; background: var(--blush); }
  .front-photo {
    left: 630px; top: 337px; width: 570px; height: 383px;
    background: linear-gradient(180deg, var(--photo-light) 0%, var(--photo-mid) 50%, var(--photo-dark) 100%);
  }
  .front-band   { left: 630px; top: 720px; width: 570px; height: 108px; background: var(--flame); }
  .front-bottom { left: 630px; top: 828px; width: 570px; height: 45px; background: var(--brick); }

  .front-title { margin: 0; font-weight: 400; }
  .front-title-line1 {
    left: 695px; top: 62px;
    font-size: 122px; line-height: 1; color: var(--paper); white-space: nowrap;
  }
  .front-title-line2 {
    left: 660px; top: 176px; width: 492px; text-align: right;
    font-size: 76px; line-height: 1; color: var(--paper); white-space: nowrap;
  }
  .front-subtitle {
    left: 695px; top: 258px; width: 453px; text-align: center;
    font-size: 30px; color: var(--ink); white-space: nowrap; letter-spacing: 0.3px;
  }
  .front-rule { left: 695px; top: 308px; width: 453px; height: 3px; background: var(--rule); }
  .front-author {
    left: 630px; top: 759px; width: 570px; text-align: center;
    font-size: 22px; color: var(--paper); letter-spacing: 1.2px; white-space: nowrap;
  }
  .divider { position: absolute; left: 830px; width: 190px; height: 6px; }
  .divider-top { top: 30px; }
  .divider-bottom { top: 848px; }
</style>
</head>
<body>
<main class="cover">
  <!-- Back -->
  <div class="block back-top"></div>
  <div class="block back-field"></div>
  <div class="block back-bottom"></div>
  <div class="block back-title script">Quiet Verses</div>
  <div class="block back-subtitle">Across Winter Evenings</div>
  <p class="block back-blurb">It is the story of a university professor told through her own songs and poems. It is about the people she loved, especially her grand children, her extensive professional and life interests, her family, friends, and festivities, her illness, etc.</p>

  <!-- Spine -->
  <div class="block spine-top"></div>
  <div class="block spine-bottom"></div>
  <div class="block spine-title">
    <span class="script">Quiet Verses</span>
    <span class="serif">Across Winter Evenings</span>
  </div>
  <div class="block spine-author">MEERA ANAND KULKARNI</div>

  <!-- Front -->
  <div class="block front-top"></div>
  <div class="block front-field"></div>
  <div class="block front-photo" role="img" aria-label="Cover photograph: a grandmother carrying a small child on her back in a grassy field at sunset"></div>
  <div class="block front-band"></div>
  <div class="block front-bottom"></div>

  <svg class="divider divider-top" viewBox="0 0 190 6" aria-hidden="true">
    <line x1="0" y1="3" x2="190" y2="3" stroke="#1c1410" stroke-width="2"/>
  </svg>
  <svg class="divider divider-bottom" viewBox="0 0 190 6" aria-hidden="true">
    <line x1="0" y1="3" x2="190" y2="3" stroke="#1c1410" stroke-width="2"/>
  </svg>

  <h1 class="front-title">
    <span class="block front-title-line1 script">Quiet</span>
    <span class="block front-title-line2 script">Verses</span>
  </h1>
  <div class="block front-subtitle">Across Winter Evenings</div>
  <div class="block front-rule"></div>
  <div class="block front-author">MEERA ANAND KULKARNI</div>
</main>
</body>
</html>
```